Dog care service needs advertising poster

Our company is Paw Haven. We provide care for dogs while their owners are away, either through home visits or a holiday stay in the homes of carefully selected minders. Our existing website & Facebook cover should provide all the colour cues for a poster - namely blues, blondes and grey. We have an existing logo (provided). We can feature the same imagery from our website as I have purchased the rights to the stock images.

www.pawhavenexample.com.au
www.facebook.com/pawhavenexampleau

This brief is for design of a poster that can be placed in vet surgeries, groomers, on community noticeboards. It should be scalable to print in three sizes, A5, A4 & A3.

We wish to clearly communicate our three areas of service "dog minding, home visits, dog walking".

We would like to have the files ready for upload to Printora (or similar) for immediate printing.

Target Market(s)

Dog owners who love their dogs like family.

Industry/Entity Type

Advertising

Font styles to use
Sans Serif

Colors
33a6d7
3276b5

Requirements
Must have
• Logo
• www.pawhavenexample.com.au
• Telephone number
• Three services - Dog Minding, Home Visits, Dog Walking
Nice to have
• use of our existing stock photography to highlight the three areas of service - Dog minding, home visits, dog walking. Existing colour palette - blues, blondes and grey.
• Text that can be used:
• Western Sydney’s complete dog care service.
• Dog Minding - Your dog stays in the home of one of our carefully selected minders.Treated like part of the family, they enjoy all the creature comforts they are used to.
• Home Visits - We visit your dog at your home for feeding, walking and playtime. Short of long visits available.
• Dog Walking - If you can't walk your dog for any reason we are here to help. 1/2 hour or hourly walks available.
• Contact us today for a tailored package to meet your needs.
Should not have
• Any additional illustrations beyond the logo.

```html
<!DOCTYPE html>
<html lang="en">
<head>
<meta charset="utf-8">
<title>Paw Haven – Dog Care Poster</title>
<link rel="stylesheet" href="https://fonts.googleapis.com/css2?family=Comfortaa:wght@400;600;700&family=Nunito:ital,wght@0,400;0,700;0,800;1,700&display=swap">
<style>
  :root{
    --page:#e8e5e0;
    --sky-top:#2f8fd0;
    --sky-mid:#8ec6ea;
    --sand:#b9b4a9;
    --sand-dark:#9e978b;
    --brand-blue:#33a6d7;
    --brand-deep:#3276b5;
    --lime:#d6e82c;
    --navy:#27265e;
    --slate:#3b4a5f;
    --ink:#1f2540;
    --white:#ffffff;
    --panel:rgba(255,255,255,0.78);
    --tagline:#8fdcf5;
    --golden:#c98f3e;
    --car:#3c5f8c;
  }
  *{box-sizing:border-box;margin:0;padding:0}
  html,body{width:1200px;height:879px;overflow:hidden;background:var(--page)}
  .poster{
    position:absolute;left:20px;top:28px;width:1160px;height:822px;overflow:hidden;
    font-family:"Comfortaa",sans-serif;color:var(--navy);
    box-shadow:0 2px 10px rgba(0,0,0,.18);
  }
  .backdrop{
    position:absolute;inset:0;
    background:linear-gradient(180deg,var(--sky-top) 0%,var(--sky-mid) 36%,#cfd6d6 44%,var(--sand) 60%,var(--sand-dark) 100%);
  }
  .hero-photo{position:absolute;left:0;top:0;width:560px;height:760px}
  .tagline{
    position:absolute;left:42px;top:42px;
    font-family:"Comfortaa",sans-serif;font-size:28px;line-height:37px;color:var(--tagline);font-weight:400;
  }
  .headline{
    position:absolute;left:264px;top:40px;white-space:nowrap;
    font-size:36px;font-weight:700;color:var(--lime);letter-spacing:-.2px;
  }
  .service-photo{
    position:absolute;top:101px;height:172px;border-radius:22px;
    border:3px solid var(--lime);box-shadow:0 0 8px rgba(214,232,44,.8);
  }
  .service-photo.minding{left:332px;width:229px;background:linear-gradient(160deg,#a9d8f1,#6fae3c 65%,#3f7a22)}
  .service-photo.visits{left:581px;width:258px;background:linear-gradient(180deg,#f1efe9 0%,#d9cfc0 45%,#7a5a3e 70%,#5a3f2a)}
  .service-photo.walking{left:860px;width:258px;background:linear-gradient(180deg,#6a8a52 0%,#94b660 45%,#5f9a2c 100%)}
  .services{
    position:absolute;left:433px;top:297px;width:696px;height:252px;
    background:var(--panel);border-radius:30px;padding:20px 22px 0 16px;
  }
  .service{display:flex;align-items:flex-start;margin-bottom:16px}
  .service:nth-child(2){margin-bottom:14px}
  .service-name{
    width:175px;flex:none;font-family:"Nunito",sans-serif;font-weight:700;font-size:22px;color:var(--navy);
    display:flex;align-items:center;gap:7px;line-height:24px;
  }
  .service-name::before{content:"";width:10px;height:10px;border-radius:50%;background:radial-gradient(circle at 35% 35%,#9aa0b0,#3d4157);flex:none}
  .service-text{font-size:17.5px;line-height:23px;color:var(--navy);text-align:justify}
  .experience{
    position:absolute;left:536px;top:578px;width:190px;text-align:center;
    font-family:"Nunito",sans-serif;font-style:italic;font-weight:700;font-size:28px;line-height:37px;color:var(--navy);
  }
  .brand{position:absolute;left:770px;top:626px;display:flex;align-items:center;gap:16px}
  .brand-dot{width:60px;height:60px;border-radius:50%;background:var(--slate)}
  .brand-name{font-family:"Comfortaa",sans-serif;font-weight:700;font-size:50px;color:var(--slate);white-space:nowrap}
  .footer-wave{position:absolute;left:0;top:0;width:1160px;height:822px}
  .cta{
    position:absolute;left:39px;top:700px;
    font-family:"Nunito",sans-serif;font-weight:800;font-size:29px;line-height:36px;color:var(--lime);
  }
  .contact-line{
    position:absolute;display:flex;align-items:center;gap:7px;
    font-family:"Nunito",sans-serif;font-size:16px;color:var(--white);white-space:nowrap;letter-spacing:.2px;
  }
  .contact-line svg{flex:none}
  .address{left:40px;top:781px}
  .email{left:514px;top:752px}
  .web{left:514px;top:782px}
  .phone{
    position:absolute;left:857px;top:760px;display:flex;align-items:center;gap:8px;
    font-family:"Nunito",sans-serif;font-weight:800;font-size:39px;color:var(--ink);white-space:nowrap;
  }
</style>
</head>
<body>
<main class="poster">
  <div class="backdrop" role="img" aria-label="Photograph of a wide sandy beach under a bright blue sky"></div>

  <svg class="hero-photo" viewBox="0 0 560 760" role="img" aria-label="Photograph of a golden retriever puppy leaning out of a blue car window">
    <defs>
      <linearGradient id="heroTone" x1="0" y1="0" x2="1" y2="1">
        <stop offset="0" stop-color="#1b1f28"/>
        <stop offset=".35" stop-color="#7a5426"/>
        <stop offset=".6" stop-color="#c98f3e"/>
        <stop offset="1" stop-color="#3c5f8c"/>
      </linearGradient>
    </defs>
    <path d="M0 0 H130 C230 90 330 230 430 420 C480 520 500 620 505 700 L505 760 H0 Z" fill="url(#heroTone)"/>
  </svg>

  <p class="tagline">Caring<br>for<br>your dog<br>like<br>family</p>

  <h1 class="headline">Western Sydney’s complete dog care service.</h1>

  <div class="service-photo minding" role="img" aria-label="Photograph of a dog sitting in long green grass"></div>
  <div class="service-photo visits" role="img" aria-label="Photograph of a small dog sitting on a home doormat"></div>
  <div class="service-photo walking" role="img" aria-label="Photograph of a bulldog on a lead walking on grass"></div>

  <section class="services">
    <div class="service">
      <h2 class="service-name">Dog Minding:</h2>
      <p class="service-text">Your dog stays in the home of one of our carefully selected minders. Treated like part of the family, they enjoy all the creature comforts they are used to.</p>
    </div>
    <div class="service">
      <h2 class="service-name">Home Visits:</h2>
      <p class="service-text">We visit your dog at your home for feeding, walking and playtime. Short of long visits available.</p>
    </div>
    <div class="service">
      <h2 class="service-name">Dog Walking:</h2>
      <p class="service-text">If you can't walk your dog for any reason we are here to help. 1/2 hour or hourly walks available.</p>
    </div>
  </section>

  <p class="experience">Over<br>20 years’<br>experience</p>

  <div class="brand">
    <span class="brand-dot"></span>
    <span class="brand-name">Paw Haven</span>
  </div>

  <svg class="footer-wave" viewBox="0 0 1160 822" aria-hidden="true">
    <defs>
      <linearGradient id="bandFill" x1="0" y1="0" x2="0" y2="1">
        <stop offset="0" stop-color="#33a6d7"/>
        <stop offset="1" stop-color="#1f8ccb"/>
      </linearGradient>
      <linearGradient id="swoosh" x1="0" y1="0" x2="1" y2="0">
        <stop offset="0" stop-color="#5a4a3c"/>
        <stop offset=".35" stop-color="#ffffff"/>
        <stop offset="1" stop-color="#ffffff" stop-opacity="0"/>
      </linearGradient>
    </defs>
    <path d="M0 720 C120 700 300 690 620 730" fill="none" stroke="url(#swoosh)" stroke-width="5"/>
    <path d="M0 690 C180 664 400 676 600 712 C800 750 1000 730 1160 670 L1160 822 L0 822 Z" fill="url(#bandFill)"/>
  </svg>

  <p class="cta">Contact us today for a tailored<br>package to meet your needs.</p>

  <p class="contact-line address">
    <svg width="12" height="16" viewBox="0 0 12 16"><path d="M6 0C2.7 0 0 2.6 0 5.9 0 10.3 6 16 6 16s6-5.7 6-10.1C12 2.6 9.3 0 6 0zm0 8.2A2.3 2.3 0 1 1 6 3.6a2.3 2.3 0 0 1 0 4.6z" fill="#ffffff"/></svg>
    Riverbend Park, New South Wales, Australia 2700
  </p>
  <p class="contact-line email">
    <svg width="22" height="14" viewBox="0 0 22 14"><rect x="1" y="1" width="20" height="12" fill="none" stroke="#ffffff" stroke-width="1.6"/><path d="M1 1l10 7 10-7" fill="none" stroke="#ffffff" stroke-width="1.6"/></svg>
    info@pawhavenexample.com.au
  </p>
  <p class="contact-line web">
    <svg width="17" height="17" viewBox="0 0 17 17" fill="none" stroke="#ffffff" stroke-width="1.4"><circle cx="8.5" cy="8.5" r="7.5"/><ellipse cx="8.5" cy="8.5" rx="3.4" ry="7.5"/><path d="M1 8.5h15M2.5 4.5h12M2.5 12.5h12"/></svg>
    www.pawhavenexample.com.au
  </p>

  <p class="phone">
    <svg width="20" height="36" viewBox="0 0 20 36"><rect x="1.5" y="5" width="17" height="29" rx="3" fill="none" stroke="#1f2540" stroke-width="2.4"/><rect x="4" y="0" width="3" height="7" fill="#1f2540"/><rect x="5" y="9" width="10" height="7" fill="#1f2540"/><g fill="#1f2540"><rect x="5" y="19" width="2.6" height="2.4"/><rect x="8.7" y="19" width="2.6" height="2.4"/><rect x="12.4" y="19" width="2.6" height="2.4"/><rect x="5" y="23.5" width="2.6" height="2.4"/><rect x="8.7" y="23.5" width="2.6" height="2.4"/><rect x="12.4" y="23.5" width="2.6" height="2.4"/><rect x="5" y="28" width="2.6" height="2.4"/><rect x="8.7" y="28" width="2.6" height="2.4"/><rect x="12.4" y="28" width="2.6" height="2.4"/></g></svg>
    0412 555 018
  </p>
</main>
</body>
</html>
```